Visitenkarten-Design für Steuerberater und Wirtschaftsprüfer
Zielgruppe
Steuerberater, Wirtschaftsprüfer in München
Aufgabenstellung
Wir haben ein Logo das uns gefällt, jetzt allerdings steht die Umfirmierung vor der Tür und aus der Kanzlei Seidelt (so unser Name) wird Seidelt und Partner mbB (die Jugend kommt mit als Partner in die Kanzlei) , Steuerberater, Wirtschaftsprüfer
Analog unseres alten Briefpapiers und der alten Visitenkarten soll eigentlich nur der Zusatz 'und Partner mbB' oder '& Partner mbB' gestaltet werden.
Das Dateiformat bei Visitenkarten bitte so übergeben, dass wir Namen selbst austauschen mit gängigen Officeprogrammen austauschen können. Bei den Visitenkarten ist das große 'Seidelt' geprägt.
Ich stelle das Logo, das aktuelle Briefpapier und aktuelle Visitenkarten ein. Unsere Farbe ist grau.
Das Logo bitte in .pdf, .png, .psd und .eps (sagt mi alles nichts, haben wir aber alles schon mal irgendwo gebraucht) , Visiten karten auch in .pddf und .ai
Bei Fragen kontaktiert mich gern jederzeit.

```html
<!DOCTYPE html>
<html lang="de">
<head>
<meta charset="utf-8">
<title>Seidelt &amp; Partner mbB – Visitenkarten</title>
<link href="https://fonts.googleapis.com/css2?family=Questrial&family=Open+Sans:wght@700&display=swap" rel="stylesheet">
<style>
  :root {
    --stage: #1e1e1e;
    --card: #5b5b5d;
    --logo: #a7a7a5;
    --watermark: #636365;
    --text-light: #c9c9c9;
    --text-bright: #ececec;
    --rule: #a9a9a9;
  }
  html, body {
    margin: 0;
    padding: 0;
    width: 1101px;
    height: 1200px;
    overflow: hidden;
    background: var(--stage);
    font-family: "Questrial", "Century Gothic", sans-serif;
  }
  .canvas {
    position: relative;
    width: 1101px;
    height: 1200px;
  }
  .card {
    position: absolute;
    background: var(--card);
    overflow: hidden;
  }
  .card--front { left: 194px; top: 96px; width: 709px; height: 471px; }
  .card--back  { left: 194px; top: 622px; width: 711px; height: 473px; }

  .wordmark {
    position: absolute;
    display: block;
    overflow: visible;
  }
  .wordmark text {
    font-family: "Questrial", "Century Gothic", sans-serif;
    fill: var(--logo);
  }
  .tagline {
    position: absolute;
    white-space: nowrap;
    color: var(--logo);
    line-height: 1;
  }
  .tagline__partner {
    font-family: "Open Sans", Arial, sans-serif;
    font-weight: 700;
    letter-spacing: 0.2px;
  }
  .tagline__services {
    font-family: "Questrial", "Century Gothic", sans-serif;
  }

  .card--front .wordmark { left: 143px; top: 52px; }
  .card--front .tagline { left: 143px; top: 148px; }
  .card--front .tagline__partner { font-size: 21px; }
  .card--front .tagline__services { font-size: 15px; }

  .card--back .wordmark { left: 105px; top: 74px; }
  .card--back .tagline { left: 105px; top: 184px; }
  .card--back .tagline__partner { font-size: 25px; }
  .card--back .tagline__services { font-size: 18px; }

  .person {
    position: absolute;
    left: 0;
    width: 100%;
    top: 270px;
    text-align: center;
    line-height: 1;
  }
  .person__degree { font-size: 15px; color: var(--text-light); }
  .person__name { font-size: 31px; color: var(--text-bright); }
  .person__title {
    display: block;
    margin-top: 4px;
    font-size: 16px;
    color: var(--text-light);
  }
  .divider {
    position: absolute;
    left: 158px;
    top: 373px;
    width: 416px;
    height: 1px;
    background: var(--rule);
  }
  .contact {
    position: absolute;
    left: 0;
    width: 100%;
    top: 392px;
    text-align: center;
    font-size: 19.5px;
    line-height: 26px;
    color: var(--text-light);
  }

  .watermark {
    position: absolute;
    left: -8px;
    top: 318px;
  }
  .watermark text {
    font-family: "Questrial", "Century Gothic", sans-serif;
    fill: var(--watermark);
  }
  .web-links {
    position: absolute;
    left: 0;
    width: 100%;
    top: 418px;
    font-size: 17px;
    color: #dcdcdc;
    white-space: nowrap;
  }
  .web-links span { position: absolute; }
</style>
</head>
<body>
<div class="canvas">

  <section class="card card--front" aria-label="Visitenkarte Vorderseite">
    <svg class="wordmark" width="430" height="90" viewBox="0 0 430 90" aria-label="Seidelt">
      <text x="0" y="82" font-size="108" textLength="430" lengthAdjust="spacingAndGlyphs">SEIDELT</text>
    </svg>
    <div class="tagline">
      <span class="tagline__partner">&amp; PARTNER mbB</span>
      <span class="tagline__services">| STEUERBERATER | WIRTSCHAFTSPRÜFER</span>
    </div>

    <div class="person">
      <span class="person__degree">Dipl.-Kfm</span>
      <span class="person__name">Lan P. Seidelt</span>
      <span class="person__title">Steuerberater/Wirtschaftsprüfer</span>
    </div>

    <div class="divider"></div>

    <div class="contact">
      Lindenhofer Straße 22&nbsp; I 80637 München<br>
      T&nbsp; 089 - 47 21 3300 I F 089 - 47 21 3309
    </div>
  </section>

  <section class="card card--back" aria-label="Visitenkarte Rückseite">
    <svg class="watermark" width="760" height="160" viewBox="0 0 760 160" aria-hidden="true">
      <text x="0" y="158" font-size="190" textLength="740" lengthAdjust="spacingAndGlyphs">SEIDELT</text>
    </svg>

    <svg class="wordmark" width="507" height="96" viewBox="0 0 507 96" aria-label="Seidelt">
      <text x="0" y="89" font-size="120" textLength="507" lengthAdjust="spacingAndGlyphs">SEIDELT</text>
    </svg>
    <div class="tagline">
      <span class="tagline__partner">&amp; PARTNER mbB</span>
      <span class="tagline__services">| STEUERBERATER | WIRTSCHAFTSPRÜFER</span>
    </div>

    <div class="web-links">
      <span style="left:76px">www.kanzlei-seidelt.de</span>
      <span style="left:330px">I</span>
      <span style="left:378px">email: info@kanzlei-seidelt.de</span>
    </div>
  </section>

</div>
</body>
</html>
```